Car finance company business card

Create a nice business card for our car financing company , Visit our website www.birchlanefinance.com for the phone number and idea of the company look. Please do not be afraid to be creative. Name on card Is Marc-Antoine Beaulieu and phone number is on our website adress of business is
27816 Boulevard Saint-Orvel,
Mirabel, QC K4R 2T8

```html
<!DOCTYPE html>
<html lang="fr">
<head>
<meta charset="utf-8">
<title>Birch Lane Finance – Business Card</title>
<link href="https://fonts.googleapis.com/css2?family=Open+Sans:wght@400;700&display=swap" rel="stylesheet">
<style>
  :root {
    --backdrop: #3b322d;
    --card-white: #f4f4f2;
    --card-black: #111111;
    --ink: #1c1c1c;
    --ink-soft: #333333;
    --divider: #cfcfcf;
    --mascot-orange: #f07a1e;
    --mascot-light: #f7a24a;
    --mascot-blue: #3f5fc4;
  }
  * { box-sizing: border-box; margin: 0; padding: 0; }
  html, body {
    width: 1200px; height: 844px; overflow: hidden;
    background: var(--backdrop);
    font-family: "Open Sans", Arial, sans-serif;
  }
  .stage {
    position: relative; width: 1200px; height: 844px;
  }
  .card {
    position: absolute; top: 272px;
    width: 520px; height: 300px;
    border-radius: 3px;
    box-shadow: 0 10px 24px rgba(0,0,0,.45);
  }
  .card--front { left: 60px; background: var(--card-white); }
  .card--back  { left: 620px; background: var(--card-black); }

  /* Front: brand block */
  .brand {
    position: absolute; left: 26px; top: 92px; width: 210px; height: 120px;
  }
  .brand__mascot {
    position: absolute; right: 0; top: 0; width: 86px; height: 90px;
    border-radius: 40% 40% 30% 30%;
    background: linear-gradient(160deg, var(--mascot-light), var(--mascot-orange) 55%, var(--mascot-blue));
  }
  .brand__name {
    position: absolute; left: 0; bottom: 0; width: 210px;
    font-weight: 700; font-size: 22px; line-height: 1.1;
    color: var(--ink);
  }
  .divider {
    position: absolute; left: 252px; top: 66px; width: 1px; height: 170px;
    background: var(--divider);
  }

  /* Front: contact block */
  .contact {
    position: absolute; left: 272px; top: 88px; width: 236px;
    color: var(--ink-soft); font-size: 13.5px; line-height: 1.35;
  }
  .contact__name {
    font-weight: 700; font-size: 15px; letter-spacing: .2px;
    color: var(--ink); text-transform: uppercase; margin-bottom: 12px;
  }
  .contact__line { display: flex; align-items: center; gap: 6px; }
  .contact__icon { width: 11px; height: 11px; flex: none; fill: var(--ink); }
  .contact__address { margin-top: 12px; }

  /* Back */
  .back__mascot {
    position: absolute; left: 185px; top: 78px; width: 150px; height: 140px;
    border-radius: 45% 45% 35% 35%;
    background: linear-gradient(160deg, var(--mascot-light), var(--mascot-orange) 55%, var(--mascot-blue));
  }
</style>
</head>
<body>
<main class="stage">
  <section class="card card--front">
    <div class="brand">
      <div class="brand__mascot" role="img" aria-label="Cartoon fox mascot in blue overalls giving a thumbs up"></div>
      <div class="brand__name">Birch Lane Finance</div>
    </div>
    <div class="divider"></div>
    <div class="contact">
      <p class="contact__name">Marc-Antoine Beaulieu</p>
      <p class="contact__line">
        <svg class="contact__icon" viewBox="0 0 24 24" aria-hidden="true"><path d="M6.6 10.8a15.1 15.1 0 0 0 6.6 6.6l2.2-2.2c.3-.3.7-.4 1-.2 1.1.4 2.3.6 3.6.6.6 0 1 .4 1 1V20c0 .6-.4 1-1 1A17 17 0 0 1 3 4c0-.6.4-1 1-1h3.5c.6 0 1 .4 1 1 0 1.3.2 2.5.6 3.6.1.3 0 .7-.2 1z"/></svg>
        (514) 555-0172
      </p>
      <p class="contact__line">
        <svg class="contact__icon" viewBox="0 0 24 24" aria-hidden="true"><path d="M12 2a10 10 0 1 0 0 20 10 10 0 0 0 0-20zm6.9 6h-2.9a15.7 15.7 0 0 0-1.4-3.6A8 8 0 0 1 18.9 8zM12 4c.8 1.2 1.5 2.5 1.9 4h-3.8c.4-1.5 1.1-2.8 1.9-4zM4.3 14a8 8 0 0 1 0-4h3.4a16 16 0 0 0 0 4zm.8 2h2.9c.3 1.3.8 2.5 1.4 3.6A8 8 0 0 1 5.1 16zM8 8H5.1a8 8 0 0 1 4.3-3.6C8.8 5.5 8.3 6.7 8 8zm4 12c-.8-1.2-1.5-2.5-1.9-4h3.8c-.4 1.5-1.1 2.8-1.9 4zm2.3-6H9.7a14.7 14.7 0 0 1 0-4h4.6a14.7 14.7 0 0 1 0 4zm.3 5.6c.6-1.1 1.1-2.3 1.4-3.6h2.9a8 8 0 0 1-4.3 3.6zm1.7-5.6a16 16 0 0 0 0-4h3.4a8 8 0 0 1 0 4z"/></svg>
        www.birchlanefinance.com
      </p>
      <p class="contact__address">27816 Boulevard Saint-Orvel,<br>Mirabel, QC K4R 2T8</p>
    </div>
  </section>

  <section class="card card--back">
    <div class="back__mascot" role="img" aria-label="Cartoon fox mascot in blue overalls holding a car key"></div>
  </section>
</main>
</body>
</html>
```